Do i have coronavirus, flue or cold?

Using information from QRV and government agencies we want to make a easy to read infographic helping patients see if they have coronavirus, the flu or a cold. Using a flow diagram or whatever you think will make it easy to read and digest for the average lamen.

Information is in the word document and in the chart.

We are www.tovipharm.co.uk attached is our brand guidelines, we will be putting this infographic on our website and email/sms it to all of our 300,000 patients.

```html
<!DOCTYPE html>
<html lang="en">
<head>
<meta charset="utf-8">
<title>Coronavirus, Flu or Cold? – Tovipharm</title>
<link href="https://fonts.googleapis.com/css2?family=Poppins:ital,wght@0,400;0,500;0,600;0,700;1,500&display=swap" rel="stylesheet">
<style>
  :root{
    --page:#eef3f4;
    --navy:#1d2150;
    --red:#f0502a;
    --blue:#2a6dd8;
    --panel:#dff0f2;
    --cell-yes:#dcf0f2;
    --cell-grey:#e2e4e6;
    --tick:#f26a2e;
    --purple:#4a2fd0;
    --text:#2b2d3a;
    --globe:#d3e4ea;
    --globe-deep:#b9d2dc;
    --skin:#f3c9b4;
    --figure:#c7dbe2;
    --decor:#e1e9eb;
    --icon-red:#e8583a;
    --icon-pink:#f4a7a0;
    --icon-blue:#6fb3de;
  }
  *{margin:0;padding:0;box-sizing:border-box}
  html,body{width:1200px;height:4072px;overflow:hidden;background:var(--page)}
  body{font-family:'Poppins',sans-serif;color:var(--text)}
  .canvas{position:relative;width:1200px;height:4072px;background:var(--page)}
  .defs{position:absolute;width:0;height:0}

  .brand{position:absolute;top:50px;left:0;width:1200px;display:flex;justify-content:center;align-items:center;gap:18px}
  .brand-dot{width:56px;height:56px;border-radius:50%;background:var(--blue)}
  .brand-name{font-size:48px;font-weight:700;color:var(--navy)}

  .hero-illustration{position:absolute;top:330px;left:200px;width:800px;height:740px;
    border-radius:380px 380px 60px 60px;
    background:linear-gradient(180deg,var(--globe) 0%,var(--globe-deep) 55%,var(--figure) 100%)}
  .title-banner{position:absolute;top:272px;left:260px;width:740px;height:170px;background:var(--red);
    color:#fff;text-align:center;padding-top:14px}
  .title-banner h1{font-size:80px;font-weight:500;line-height:1.05}
  .title-banner p{font-size:44px;font-weight:400;line-height:1.2}

  .intro{position:absolute;top:1140px;left:0;width:1200px;text-align:center;color:var(--blue);
    font-size:26px;font-weight:600;line-height:1.6;white-space:nowrap}

  .symptom-panel{position:absolute;top:1288px;left:48px;width:1100px;height:280px;background:var(--panel);border-radius:14px}
  .symptom-panel h2{position:absolute;top:44px;left:44px;font-size:56px;font-weight:700;color:var(--navy);white-space:nowrap}
  .symptom-panel p{position:absolute;top:136px;left:44px;width:780px;font-size:25px;line-height:1.5;color:var(--text)}
  .doctor-illustration{position:absolute;top:1260px;left:940px;width:160px;height:360px;border-radius:80px 80px 20px 20px;
    background:linear-gradient(180deg,var(--globe),var(--globe-deep))}

  .chart{position:absolute;top:1692px;left:40px;width:1120px}
  .chart-head,.row{display:grid;grid-template-columns:330px 252px 252px 252px;column-gap:12px;align-items:center}
  .chart-head{height:108px;background:var(--navy);color:#fff;font-size:30px;font-weight:400}
  .chart-head span{text-align:center}
  .chart-head .col-corona{font-weight:600}
  .row{height:160px}
  .symptom{display:flex;align-items:center;gap:28px;padding-left:20px;font-size:27px;font-weight:600;color:var(--navy);line-height:1.2}
  .symptom-icon{flex:none;width:70px;height:70px}
  .cell{position:relative;height:120px;display:flex;flex-direction:column;justify-content:center;align-items:center;
    font-size:40px;font-weight:600;color:var(--navy);line-height:1.05}
  .cell.yes{background:var(--cell-yes)}
  .cell.grey{background:var(--cell-grey);font-size:28px;font-weight:500;color:var(--text)}
  .cell small{font-size:20px;font-weight:500;font-style:italic;margin-top:4px}
  .tick{position:absolute;top:-16px;left:50%;margin-left:-24px;width:48px;height:48px}
  .cell.ticked{padding-top:22px}

  .virus-decoration{position:absolute;top:3300px;left:660px;width:460px;height:320px}

  .nurse-illustration{position:absolute;top:3420px;left:60px;width:140px;height:380px;border-radius:70px 70px 20px 20px;
    background:linear-gradient(180deg,var(--globe),var(--globe-deep))}
  .protect-title{position:absolute;top:3660px;left:260px;font-size:56px;font-weight:700;color:var(--purple);line-height:1.2}
  .protect-copy{position:absolute;top:3750px;left:260px;width:860px;font-size:25px;line-height:44px;color:var(--text)}
</style>
</head>
<body>
<div class="canvas">

  <svg class="defs" aria-hidden="true">
    <symbol id="tick" viewBox="0 0 48 48">
      <circle cx="24" cy="24" r="22" fill="var(--tick)"/>
      <polyline points="14,25 21,32 34,17" fill="none" stroke="#fff" stroke-width="5" stroke-linecap="round" stroke-linejoin="round"/>
    </symbol>
  </svg>

  <header class="brand">
    <span class="brand-dot"></span>
    <span class="brand-name">Tovipharm</span>
  </header>

  <div class="hero-illustration" role="img" aria-label="Illustration of people wearing face masks standing in front of a globe with virus particles"></div>
  <div class="title-banner">
    <h1>Coronavirus</h1>
    <p>Covid-19 or 2019-nCov</p>
  </div>

  <p class="intro">On 11 February 2020 the QRV gave the disease caused by the new<br>coronavirus an official name: COVID-19, short for coronavirus disease 2019.</p>

  <section class="symptom-panel">
    <h2>Do I have the sympthoms?</h2>
    <p>The symptoms can vary in severity.<br>Some people become infected but don't develop any<br>symptoms and don't feel unwell.</p>
  </section>
  <div class="doctor-illustration" role="img" aria-label="Illustration of a doctor holding a magnifying glass"></div>

  <section class="chart">
    <div class="chart-head">
      <span>Symptom</span>
      <span class="col-corona">Coronavirus</span>
      <span>Flu</span>
      <span>Cold</span>
    </div>

    <div class="row">
      <div class="symptom">
        <svg class="symptom-icon" viewBox="0 0 70 70" aria-hidden="true"><rect x="29" y="8" width="12" height="38" rx="6" fill="#fff" stroke="var(--icon-red)" stroke-width="3"/><rect x="32" y="22" width="6" height="26" fill="var(--icon-red)"/><circle cx="35" cy="52" r="10" fill="var(--icon-red)"/></svg>
        Fever</div>
      <div class="cell yes ticked"><svg class="tick"><use href="#tick"/></svg>Yes</div>
      <div class="cell yes ticked"><svg class="tick"><use href="#tick"/></svg>Yes<small>High</small></div>
      <div class="cell grey">Rare</div>
    </div>

    <div class="row">
      <div class="symptom">
        <svg class="symptom-icon" viewBox="0 0 70 70" aria-hidden="true"><circle cx="22" cy="36" r="14" fill="var(--icon-blue)"/><circle cx="42" cy="28" r="10" fill="var(--icon-blue)" opacity=".7"/><circle cx="54" cy="42" r="7" fill="var(--icon-blue)" opacity=".5"/><circle cx="60" cy="24" r="4" fill="var(--icon-blue)" opacity=".4"/></svg>
        Cough</div>
      <div class="cell yes ticked"><svg class="tick"><use href="#tick"/></svg>Yes<small>Dry cough</small></div>
      <div class="cell yes ticked"><svg class="tick"><use href="#tick"/></svg>Yes</div>
      <div class="cell grey">Moderate</div>
    </div>

    <div class="row">
      <div class="symptom">
        <svg class="symptom-icon" viewBox="0 0 70 70" aria-hidden="true"><text x="8" y="58" font-family="Poppins,sans-serif" font-weight="700" font-size="30" fill="var(--navy)">z</text><text x="28" y="40" font-family="Poppins,sans-serif" font-weight="700" font-size="40" fill="var(--navy)">Z</text></svg>
        Tiredness</div>
      <div class="cell yes ticked"><svg class="tick"><use href="#tick"/></svg>Yes</div>
      <div class="cell yes ticked"><svg class="tick"><use href="#tick"/></svg>Yes</div>
      <div class="cell grey">Mild</div>
    </div>

    <div class="row">
      <div class="symptom">
        <svg class="symptom-icon" viewBox="0 0 70 70" aria-hidden="true"><path d="M35 8v24M35 32l-8 6M35 32l8 6" stroke="var(--icon-red)" stroke-width="4" fill="none" stroke-linecap="round"/><path d="M28 24c-12 0-20 14-20 30 0 6 6 8 12 6l10-4V30z" fill="var(--icon-pink)"/><path d="M42 24c12 0 20 14 20 30 0 6-6 8-12 6l-10-4V30z" fill="var(--icon-pink)"/></svg>
        Shortness<br>of breath</div>
      <div class="cell yes ticked"><svg class="tick"><use href="#tick"/></svg>Yes</div>
      <div class="cell yes ticked"><svg class="tick"><use href="#tick"/></svg>Yes</div>
      <div class="cell grey">Rare</div>
    </div>

    <div class="row">
      <div class="symptom">
        <svg class="symptom-icon" viewBox="0 0 70 70" aria-hidden="true"><path d="M8 62c2-20 12-30 27-30s25 10 27 30z" fill="var(--skin)"/><path d="M40 6 28 30h10l-6 20 16-28H38z" fill="var(--icon-red)"/></svg>
        Muscle<br>aches</div>
      <div class="cell yes ticked"><svg class="tick"><use href="#tick"/></svg>Yes</div>
      <div class="cell yes ticked"><svg class="tick"><use href="#tick"/></svg>Yes<small>Often</small></div>
      <div class="cell grey">Moderate</div>
    </div>

    <div class="row">
      <div class="symptom">
        <svg class="symptom-icon" viewBox="0 0 70 70" aria-hidden="true"><circle cx="35" cy="38" r="24" fill="var(--icon-red)"/><path d="M30 22l8 8-6 4 8 10" stroke="#fff" stroke-width="4" fill="none" stroke-linecap="round" stroke-linejoin="round"/></svg>
        Headache</div>
      <div class="cell grey">Sometimes</div>
      <div class="cell yes ticked"><svg class="tick"><use href="#tick"/></svg>Yes</div>
      <div class="cell grey">Rare</div>
    </div>

    <div class="row">
      <div class="symptom">
        <svg class="symptom-icon" viewBox="0 0 70 70" aria-hidden="true"><path d="M24 6h22v58H24z" fill="var(--skin)"/><circle cx="35" cy="36" r="8" fill="var(--icon-red)"/><circle cx="35" cy="36" r="14" fill="none" stroke="var(--icon-red)" stroke-width="2" opacity=".5"/></svg>
        Sore<br>throat</div>
      <div class="cell grey">Sometimes</div>
      <div class="cell grey">Sometimes</div>
      <div class="cell yes ticked"><svg class="tick"><use href="#tick"/></svg>Yes</div>
    </div>

    <div class="row">
      <div class="symptom">
        <svg class="symptom-icon" viewBox="0 0 70 70" aria-hidden="true"><path d="M35 8C26 24 20 34 20 44a15 15 0 0 0 30 0c0-10-6-20-15-36z" fill="var(--icon-blue)"/></svg>
        Stuffy or<br>runny<br>nose</div>
      <div class="cell grey">Rare</div>
      <div class="cell grey">Sometimes</div>
      <div class="cell yes ticked"><svg class="tick"><use href="#tick"/></svg>Yes</div>
    </div>

    <div class="row">
      <div class="symptom">
        <svg class="symptom-icon" viewBox="0 0 70 70" aria-hidden="true"><circle cx="14" cy="35" r="8" fill="var(--icon-blue)"/><circle cx="34" cy="22" r="5" fill="var(--icon-blue)"/><circle cx="36" cy="40" r="6" fill="var(--icon-blue)"/><circle cx="52" cy="30" r="4" fill="var(--icon-blue)"/><circle cx="54" cy="50" r="4" fill="var(--icon-blue)"/><circle cx="62" cy="16" r="3" fill="var(--icon-blue)"/></svg>
        Sneezing</div>
      <div class="cell grey">No</div>
      <div class="cell grey">Sometimes</div>
      <div class="cell yes ticked"><svg class="tick"><use href="#tick"/></svg>Yes</div>
    </div>
  </section>

  <svg class="virus-decoration" viewBox="0 0 460 320" role="img" aria-label="Faint virus particle decoration">
    <circle cx="150" cy="150" r="110" fill="var(--decor)"/>
    <circle cx="360" cy="220" r="70" fill="var(--decor)"/>
  </svg>

  <div class="nurse-illustration" role="img" aria-label="Illustration of a nurse holding a syringe"></div>
  <h2 class="protect-title">Protect Yourself</h2>
  <p class="protect-copy">Everyday preventive actions to help prevent the spread of the virus. Those actions include: Clean your hands often, avoid close contact with people who are sick, stay home and wear a face-mask if you're sick, Cover coughs and sneeze.</p>

</div>
</body>
</html>
```